Global Voltara Power Systems Technology Company needs initial Web Design

We need a web design for new Voltara Power Systems Technology company. The company has developed innovative technology and needs a website to reflect this branding. Whilst this assignment will represent the initial site we are seeking an ongoing relationship to allow the website to be developed as the business develops. The logo design and initial artwork has been done and needs to incorporated in the design.

Target Market(s)

Business decision makers and power generation companies
Initially two target markets
1. Commercial users like construction companies or industrial businesses like mining that currently utilize Diesel generators to create power
2. Electrical power suppliers that currently use diesel generators in regional and remote to supply remote communities like outback Australia or pacific islands like Fuji etc
The purpose initially is to showcase/ educate customers about the product but we ideally would like to capture email addressees as part of this process.

The product information has been limited at this stage as we are currently finalizing IP registrations.

The main competitors are
1 Solar energy products but these only generate power when the sun is shinning and needs to be stored which battery technology is expensive and will only last up to 3 days at most
2 Wind energy would the same as as solar
3 Diesel generators run continually but are expensive to operate. Our product would be approximately 1/2 the operating cost of this energy source. There is no reliance on fuel sources so the user doesn't need to store fuel, worry about running out or fluctuations in fuel pricing. Diesel generators are very noisy and not environmentally friendly.

Industry/Entity Type

Solar Energy

Coding

Coded - Design and coding required

Number of Pages Required

4 page

Font styles to use
Sans Serif

Colors
acd036
33a6d7
ffffff

Requirements
Must have
• This version is intended as an initial basic 4 page website only.
• It should be built on the basis that it can be expanded after the products are formally launched into the market. A separate assignment will be allocated to the successful initial website designer to create a more elaborate site with a budget to match. The format and content for the initial site is outlined in the attached word document (File 1) The remaining files contain the logo and existing artwork and associated colours. The site should have the ability to view on smart phones and tablets.

```html
<!DOCTYPE html>
<html lang="en">
<head>
<meta charset="utf-8">
<title>Voltara Power Systems</title>
<link href="https://fonts.googleapis.com/css2?family=Open+Sans:wght@300;400;600;700&family=Arimo:wght@400;700&display=swap" rel="stylesheet">
<style>
:root{
  --blue-deep:#164e98;
  --blue-mid:#2a73c4;
  --blue-light:#63b4f0;
  --heading:#1b5fa9;
  --button:#1e5ea8;
  --green:#8cbf2f;
  --text:#6a6a6a;
  --dark:#333;
  --footer:#272727;
  --footer-base:#1d1d1d;
  --footer-text:#b9b9b9;
  --white:#fff;
}
*{margin:0;padding:0;box-sizing:border-box}
html,body{width:867px;height:1200px;overflow:hidden;background:var(--white)}
body{position:relative;font-family:"Open Sans",sans-serif;color:var(--text)}
.abs{position:absolute}
.hero{left:0;top:0;width:867px;height:320px;background:radial-gradient(ellipse at 60% 55%,var(--blue-light) 0%,var(--blue-mid) 45%,var(--blue-deep) 100%);overflow:hidden}
.nav-band{left:0;top:0;width:867px;height:51px;background:rgba(16,60,125,.55)}
.hero-curve{left:0;top:0}
.brand{left:28px;top:34px;width:150px;text-align:center}
.brand-mark{width:56px;height:56px;border-radius:50%;background:var(--green);margin:0 auto 8px}
.brand-name{font-weight:700;font-size:15px;line-height:1.15;color:var(--blue-mid);letter-spacing:.5px}
.nav{left:320px;top:12px;display:flex}
.nav-item{width:124px;height:26px;border-right:1px solid rgba(255,255,255,.25);color:var(--white)}
.nav-item b{display:block;font-size:10px;font-weight:700}
.nav-item span{display:block;font-size:8px;margin-top:2px}
.nav-item+.nav-item{padding-left:18px}
.hero-kicker{left:223px;top:133px;font-size:18px;font-weight:700;color:var(--white)}
.hero-title{left:222px;top:154px;font-size:31px;font-weight:300;color:var(--white)}
.btn{display:flex;align-items:center;justify-content:center;color:var(--white);font-size:8px;text-transform:uppercase}
.btn-green{left:224px;top:203px;width:115px;height:32px;background:var(--green)}
.hero-arrows{left:228px;top:248px;color:rgba(255,255,255,.4);font-size:12px}
.hero-product{left:488px;top:78px;width:318px;height:208px;border-radius:6px;background:linear-gradient(135deg,#e9eef1 0%,#c9d3d8 50%,#3aa7d8 100%);opacity:.9}
.h2{color:var(--heading);font-weight:700;text-transform:uppercase}
.welcome-title{left:0;width:867px;top:357px;text-align:center;font-size:14px}
.welcome-text{left:170px;width:527px;top:384px;text-align:center;font-size:8px;line-height:16px}
.range-title{left:71px;top:457px;font-size:13px}
.range-text{left:71px;top:486px;font-size:8.5px}
.btn-blue{background:var(--button);border-radius:2px}
.btn-more{left:661px;top:470px;width:134px;height:31px}
.card{top:523px;width:170px}
.card-img{height:162px;border:1px solid #cfcfcf;background:radial-gradient(circle at 50% 45%,#ffffff 0%,#e6e6e6 60%,#cfcfcf 100%)}
.card-name{margin-top:13px;text-align:center;font-size:12px;font-weight:700;color:var(--heading)}
.card-sub{margin-top:1px;text-align:center;font-size:8.5px;color:var(--dark)}
.about-photo{left:71px;top:779px;width:230px;height:167px;background:linear-gradient(90deg,#8fa9b5 0%,#c6d8e2 50%,#9fc0d6 100%)}
.about-title{left:333px;top:774px;font-size:13px}
.about-text{left:333px;top:800px;width:462px;font-size:7.6px;line-height:16px}
.about-text p+p{margin-top:16px}
.btn-info{left:334px;top:911px;width:110px;height:34px}
.footer{left:0;top:993px;width:867px;height:171px;background:var(--footer);font-family:"Arimo",sans-serif}
.footer-base{left:0;top:1164px;width:867px;height:36px;background:var(--footer-base);font-family:"Arimo",sans-serif;color:var(--footer-text);font-size:7px;text-align:center;line-height:36px}
.f-head{top:28px;color:var(--white);font-family:"Open Sans",sans-serif;font-weight:700;font-size:8.5px;text-transform:uppercase}
.f-col{top:52px;color:var(--footer-text);font-size:7px}
.f-about{left:84px;width:232px;line-height:16.7px}
.f-list li{list-style:none;height:18.5px}
.f-info li{height:16px}
.f-social li{list-style:none;display:flex;align-items:center;height:25px}
.f-social i{width:17px;height:17px;border:1px solid #555;margin-right:6px}
</style>
</head>
<body>
<div class="abs hero">
  <div class="abs nav-band"></div>
  <div class="abs hero-product" role="img" aria-label="Two white and blue power generator units"></div>
  <div class="abs hero-kicker">Voltara Power Systems</div>
  <div class="abs hero-title">The Ultimate Power</div>
  <div class="abs btn btn-green">View all products</div>
  <div class="abs hero-arrows">‹ ›</div>
  <svg class="abs hero-curve" width="867" height="320" viewBox="0 0 867 320"><path d="M0 0H252C226 115 140 218 28 247C122 250 200 282 237 320H0Z" fill="#fff"/></svg>
  <div class="abs brand"><div class="brand-mark"></div><div class="brand-name">VOLTARA POWER SYSTEMS</div></div>
  <nav class="abs nav">
    <div class="nav-item"><b>HOME</b><span>Welcome to our site</span></div>
    <div class="nav-item"><b>OUR PRODUCTS</b><span>View our products</span></div>
    <div class="nav-item"><b>OUR PEOPLES</b><span>Know our Team</span></div>
    <div class="nav-item"><b>CONTACT US</b><span>Get in Touch</span></div>
  </nav>
</div>

<h2 class="abs h2 welcome-title">Welcome to Voltara Power Systems</h2>
<p class="abs welcome-text">Voltara Power Systems has developed patented electric power generation technology that revolutionises the way the world will think about power generation for generations to come.</p>

<h2 class="abs h2 range-title">Voltara Power Systems -The Ultimate Power</h2>
<p class="abs range-text">Voltara Power Systems has developed patented electric power generation technology that revolutionises the way the world</p>
<div class="abs btn btn-blue btn-more">View more products</div>

<div class="abs card" style="left:71px"><div class="card-img" role="img" aria-label="Generator unit Summit 100"></div><div class="card-name">SUMMIT 100</div><div class="card-sub">100 KILOWATTS</div></div>
<div class="abs card" style="left:256px"><div class="card-img" role="img" aria-label="Generator unit Summit 250KW"></div><div class="card-name">SUMMIT 250KW</div><div class="card-sub">250 KILOWATTS</div></div>
<div class="abs card" style="left:441px"><div class="card-img" role="img" aria-label="Generator unit Summit 500KW"></div><div class="card-name">SUMMIT 500KW</div><div class="card-sub">500 KILOWATTS</div></div>
<div class="abs card" style="left:626px"><div class="card-img" role="img" aria-label="Generator unit Summit 1000"></div><div class="card-name">SUMMIT 1000</div><div class="card-sub">1 MEGAWATT</div></div>

<div class="abs about-photo" role="img" aria-label="Smiling team member in an office"></div>
<h2 class="abs h2 about-title">About Voltara Power Systems</h2>
<div class="abs about-text">
  <p>Voltara Power Systems has developed patented electric power generation technology that revolutionises the way the world will think about power generation for generations to come.</p>
  <p>The advanced generator technology has been designed in a way that there are minimal energy losses. The generator, coupled with the intelligent mechanical and electronic multipliers, allows the system to produce very high input to output ratios resulting in ratios of 1 to 100 outputs.</p>
</div>
<div class="abs btn btn-blue btn-info">View more info</div>

<footer class="abs footer">
  <div class="abs f-head" style="left:85px">What we do ?</div>
  <p class="abs f-col f-about">Lorem Ipsum is simply dummy text of the printing and typesetting industry. Lorem Ipsum has been the industry's standard dummy text ever since the 1500s, when an unknown printer took a galley of type and scrambled it to make a type specimen book. It has survived not only five centuries, but also the leap into electronic...</p>
  <div class="abs f-head" style="left:383px">Welcome</div>
  <ul class="abs f-col f-list" style="left:383px;top:51px"><li>Home</li><li>Our products</li><li>Our Peoples</li><li>Contact us</li></ul>
  <div class="abs f-head" style="left:521px">Information</div>
  <ul class="abs f-col f-list f-info" style="left:521px;top:51px"><li>Privacy Policy</li><li>Terms &amp; Conditions</li><li>Sitemap</li></ul>
  <div class="abs f-head" style="left:675px">Follow us</div>
  <ul class="abs f-col f-social" style="left:677px;top:52px"><li><i></i>: Friendwall</li><li><i></i>Chirpline</li><li><i></i>: Circlepost</li><li><i></i>: Clipstream</li></ul>
</footer>
<div class="abs footer-base">© 2015. Voltara Power Systems. All rights reserved.</div>
</body>
</html>
```